Powerpoint design for Summit Lane Advisors

We would like to have a Power point template/design with flexibilities and good opportunities to do changes.
• Be able to change in image background
• Themes are SLA colors and complementary colors. Please come with suggestions.
• Alternate white and blue background
• Standard functions and opportunities within Powerpoint should be able to be used or be accessible.
• Feel free to change/alter the logo for example remove or separate the text in the logo ("Summit Lane Advisors" ) and the tagline ("we create competitiveness")
• www.summitlaneadvisors.se

```html
<!DOCTYPE html>
<html lang="en">
<head>
<meta charset="utf-8">
<title>Summit Lane Advisors – Presentation Template</title>
<link rel="stylesheet" href="https://fonts.googleapis.com/css2?family=Lato:ital,wght@0,400;0,700;0,900;1,900&display=swap">
<style>
  :root {
    --brand-blue: #123c88;
    --brand-deep: #0c2d6b;
    --brand-ink: #0f3a86;
    --paper: #ededed;
    --paper-light: #f4f4f4;
    --white: #ffffff;
    --text-dark: #222a38;
    --rule-light: rgba(255,255,255,0.55);
    --rule-dark: #b9c0cc;
  }
  * { box-sizing: border-box; margin: 0; padding: 0; }
  html, body { width: 1200px; height: 4212px; overflow: hidden; background: var(--white); }
  body { position: relative; font-family: "Lato", sans-serif; color: var(--white); }
  .slide { position: absolute; left: 0; width: 1200px; overflow: hidden; }

  .brand-mark { position: absolute; font-weight: 900; color: var(--white); letter-spacing: 2px; line-height: 1; }
  .brand-name { position: absolute; left: 0; width: 100%; text-align: center; font-weight: 400; line-height: 1; }
  .brand-tagline { position: absolute; left: 0; width: 100%; text-align: center; letter-spacing: 4px; line-height: 1; }

  /* Slide footer */
  .slide-footer { position: absolute; left: 87px; width: 1030px; height: 36px; }
  .slide-footer .footer-mark { position: absolute; left: 0; top: 6px; font-size: 24px; font-weight: 900; letter-spacing: 1px; }
  .slide-footer .footer-rule { position: absolute; left: 80px; right: 36px; top: 18px; height: 1px; }
  .slide-footer .page-no { position: absolute; right: 0; top: 0; width: 36px; height: 36px; border-radius: 50%; font-size: 16px; font-weight: 700; display: flex; align-items: center; justify-content: center; }
  .footer-on-dark .footer-mark { color: var(--white); }
  .footer-on-dark .footer-rule { background: var(--rule-light); }
  .footer-on-light .footer-mark { color: var(--brand-ink); }
  .footer-on-light .footer-rule { background: var(--rule-dark); }
  .page-no.filled { background: var(--brand-deep); color: var(--white); }
  .page-no.inverse { background: var(--white); color: var(--brand-deep); }

  /* Slide 1 – cover */
  .cover { top: 0; height: 664px; background: var(--paper); }
  .cover .band { position: absolute; left: 0; top: 0; width: 1200px; height: 432px; background: var(--brand-blue); }
  .cover .hero-photo { position: absolute; left: 615px; top: 69px; width: 511px; height: 515px;
    background: radial-gradient(circle at 50% 45%, #e9a152 0%, #6a4c5a 30%, #23375f 55%, #1b2c4e 100%); }
  .cover .headline { position: absolute; left: 75px; top: 482px; font-size: 44px; font-weight: 900; font-style: italic; color: var(--brand-ink); line-height: 54px; }

  /* Slide 2 */
  .transformation { top: 710px; height: 663px; background: var(--brand-blue); }
  .transformation .visual { position: absolute; left: 690px; top: 0; width: 510px; height: 663px;
    background: radial-gradient(circle at 55% 45%, #2f8fe0 0%, #164a9e 40%, #0a1f55 80%, #071640 100%); }
  .transformation h2 { position: absolute; left: 75px; top: 88px; font-size: 48px; font-weight: 700; line-height: 52px; }
  .transformation .body { position: absolute; left: 75px; top: 213px; width: 600px; font-size: 15.5px; line-height: 30.5px; }
  .transformation .body p { margin-bottom: 8px; }

  /* Slide 3 – services */
  .services { top: 1421px; height: 664px; background: linear-gradient(180deg, var(--paper) 0%, var(--paper-light) 100%); }
  .services .band { position: absolute; left: 0; top: 0; width: 1200px; height: 353px; background: var(--brand-blue); }
  .service-card { position: absolute; top: 196px; width: 242px; height: 358px; background: var(--white); border-radius: 8px;
    box-shadow: 0 3px 10px rgba(0,0,0,0.18); text-align: center; color: var(--text-dark); }
  .service-card svg { position: absolute; left: 87px; top: 45px; }
  .service-card h3 { position: absolute; left: 0; top: 134px; width: 100%; font-size: 25px; font-weight: 700; color: var(--brand-ink); line-height: 30px; }
  .service-card p { position: absolute; left: 24px; right: 24px; font-size: 13.5px; line-height: 25px; }

  /* Slide 4 – focus areas */
  .focus { top: 2132px; height: 664px;
    background: linear-gradient(180deg, #1d3f7a 0%, #163568 45%, #102a58 100%); }
  .focus h2 { position: absolute; left: 0; top: 48px; width: 100%; text-align: center; font-size: 44px; font-weight: 700; }
  .focus-col { position: absolute; top: 138px; }
  .focus-col h3 { font-size: 37px; font-weight: 700; line-height: 46px; margin-bottom: 17px; }
  .focus-col li { list-style: none; font-size: 22px; line-height: 42.5px; display: flex; align-items: center; gap: 10px; }
  .focus-col li svg { flex: none; }

  /* Slide 5 */
  .feature { top: 2840px; height: 664px; background: #e6e6e8; }
  .feature .band { position: absolute; left: 0; top: 0; width: 497px; height: 664px; background: var(--brand-blue); }
  .feature .photo { position: absolute; left: 51px; top: 85px; width: 538px; height: 492px;
    background: radial-gradient(circle at 45% 50%, #c9c5c0 0%, #8c7e78 45%, #3e4652 100%); }
  .feature h2 { position: absolute; left: 616px; top: 210px; font-size: 48px; font-weight: 900; color: var(--brand-ink); line-height: 52px; }
  .feature .body { position: absolute; left: 616px; top: 333px; width: 470px; font-size: 15.5px; line-height: 30.5px; color: var(--text-dark); }

  /* Slide 6 – contact */
  .contact { top: 3551px; height: 661px;
    background: linear-gradient(180deg, #17387a 0%, #10306b 55%, #0b2558 100%); }
  .contact .contact-line { position: absolute; left: 0; width: 100%; text-align: center; font-size: 22px; display: flex; justify-content: center; align-items: center; gap: 14px; }
</style>
</head>
<body>

<!-- Slide 1 -->
<section class="slide cover">
  <div class="band"></div>
  <div class="brand-mark" style="left:212px; top:130px; font-size:104px;">SLA</div>
  <div class="brand-name" style="top:254px; width:655px; font-size:45px;">Summit Lane Advisors</div>
  <div class="brand-tagline" style="top:307px; width:655px; font-size:24px;">We create competitiveness</div>
  <div class="hero-photo" role="img" aria-label="Two business people shaking hands in silhouette before a city skyline at sunset, framed by a circle"></div>
  <div class="headline">We Create<br>Digital Competitiveness</div>
</section>

<!-- Slide 2 -->
<section class="slide transformation">
  <div class="visual" role="img" aria-label="Glowing blue low-poly digital butterfly on a dark blue background"></div>
  <h2>Digital Development<br>&amp; Transformation</h2>
  <div class="body">
    <p>Digital transformation is changing the way we live, what we<br>do and how we communicate with each other as well as how<br>we do our business and shopping.</p>
    <p>The customers are better informed and more independent in<br>their decisions. The digital transformation has created great<br>possibilities in more channels than ever.</p>
    <p>To get knowledge about how products, services and information can be<br>consumed with digital concepts and solutions is more necessary than ever for<br>companies. They need this to adapt to their customers wishes<br>and requirements.</p>
  </div>
  <div class="slide-footer footer-on-dark" style="top:595px;">
    <span class="footer-mark">SLA</span><span class="footer-rule"></span><span class="page-no filled">2</span>
  </div>
</section>

<!-- Slide 3 -->
<section class="slide services">
  <div class="band"></div>
  <div class="brand-mark" style="left:516px; top:78px; font-size:70px;">SLA</div>

  <article class="service-card" style="left:75px;">
    <svg width="68" height="62" viewBox="0 0 68 62"><path d="M24 10V4h20v6" fill="none" stroke="#222" stroke-width="5"/><rect x="2" y="12" width="64" height="48" rx="5" fill="#222"/><rect x="17" y="12" width="4" height="48" fill="#fff"/><rect x="47" y="12" width="4" height="48" fill="#fff"/></svg>
    <h3>Our Passion</h3>
    <p style="top:178px;">Summit Lane Advisors’ passion is to understand and follow the digital transformation and development and to use this knowledge.</p>
  </article>

  <article class="service-card" style="left:345px;">
    <svg width="68" height="70" viewBox="0 0 68 70"><path d="M34 2a22 22 0 0 0-13 40c2 2 3 5 3 8h20c0-3 1-6 3-8A22 22 0 0 0 34 2z" fill="#222"/><rect x="24" y="54" width="20" height="5" rx="2" fill="#222"/><rect x="26" y="62" width="16" height="6" rx="3" fill="#222"/></svg>
    <h3>Concept<br>Development</h3>
    <p style="top:204px;">Together with our customers we identify the business opportunities and challenges and develop concepts according to this.</p>
  </article>

  <article class="service-card" style="left:615px;">
    <svg width="68" height="68" viewBox="0 0 68 68"><path d="M10 30a24 24 0 0 1 42-13" fill="none" stroke="#222" stroke-width="8"/><path d="M60 4v22H38z" fill="#222"/><path d="M58 38a24 24 0 0 1-42 13" fill="none" stroke="#222" stroke-width="8"/><path d="M8 64V42h22z" fill="#222"/></svg>
    <h3>Concept<br>Implementation</h3>
    <p style="top:204px;">New concepts and solutions are very dependent on a good implementation plan to be successful. Together with the customer we work.</p>
  </article>

  <article class="service-card" style="left:885px;">
    <svg width="68" height="56" viewBox="0 0 68 56"><path d="M3 2v51h63" fill="none" stroke="#222" stroke-width="5"/><rect x="14" y="26" width="8" height="22" fill="#222"/><rect x="27" y="14" width="8" height="34" fill="#222"/><rect x="40" y="30" width="8" height="18" fill="#222"/><rect x="53" y="8" width="8" height="40" fill="#222"/></svg>
    <h3>Analytics and<br>Evaluation</h3>
    <p style="top:204px;">Before, during and after concept development it is crucial to regularly do analytics and evaluation.</p>
  </article>

  <div class="slide-footer footer-on-light" style="top:603px;">
    <span class="footer-mark">SLA</span><span class="footer-rule"></span><span class="page-no filled">3</span>
  </div>
</section>

<!-- Slide 4 -->
<section class="slide focus" role="img" aria-label="Blurred supermarket aisle with a shopping cart, tinted deep blue">
  <h2>Focus Areas</h2>
  <div class="focus-col" style="left:75px;">
    <h3>We work with the following<br>in digital development</h3>
    <ul>
      <li><svg width="22" height="22" viewBox="0 0 22 22"><circle cx="11" cy="11" r="9.5" fill="none" stroke="#fff" stroke-width="2"/><path d="M6.5 11.5l3 3 6-6.5" fill="none" stroke="#fff" stroke-width="2"/></svg>Customer and user experience</li>
      <li><svg width="22" height="22" viewBox="0 0 22 22"><circle cx="11" cy="11" r="9.5" fill="none" stroke="#fff" stroke-width="2"/><path d="M6.5 11.5l3 3 6-6.5" fill="none" stroke="#fff" stroke-width="2"/></svg>Systems and solutions in store</li>
      <li><svg width="22" height="22" viewBox="0 0 22 22"><circle cx="11" cy="11" r="9.5" fill="none" stroke="#fff" stroke-width="2"/><path d="M6.5 11.5l3 3 6-6.5" fill="none" stroke="#fff" stroke-width="2"/></svg>Digital development &nbsp;and transformation</li>
      <li><svg width="22" height="22" viewBox="0 0 22 22"><circle cx="11" cy="11" r="9.5" fill="none" stroke="#fff" stroke-width="2"/><path d="M6.5 11.5l3 3 6-6.5" fill="none" stroke="#fff" stroke-width="2"/></svg>Digitalization and technology</li>
    </ul>
  </div>
  <div class="focus-col" style="left:628px;">
    <h3>We work with the following<br>technologies</h3>
    <ul>
      <li><svg width="22" height="22" viewBox="0 0 22 22"><circle cx="11" cy="11" r="9.5" fill="none" stroke="#fff" stroke-width="2"/><path d="M6.5 11.5l3 3 6-6.5" fill="none" stroke="#fff" stroke-width="2"/></svg>Digital Signage</li>
      <li><svg width="22" height="22" viewBox="0 0 22 22"><circle cx="11" cy="11" r="9.5" fill="none" stroke="#fff" stroke-width="2"/><path d="M6.5 11.5l3 3 6-6.5" fill="none" stroke="#fff" stroke-width="2"/></svg>Sound solutions</li>
      <li><svg width="22" height="22" viewBox="0 0 22 22"><circle cx="11" cy="11" r="9.5" fill="none" stroke="#fff" stroke-width="2"/><path d="M6.5 11.5l3 3 6-6.5" fill="none" stroke="#fff" stroke-width="2"/></svg>Queue management solutions</li>
      <li><svg width="22" height="22" viewBox="0 0 22 22"><circle cx="11" cy="11" r="9.5" fill="none" stroke="#fff" stroke-width="2"/><path d="M6.5 11.5l3 3 6-6.5" fill="none" stroke="#fff" stroke-width="2"/></svg>People counter technology</li>
      <li><svg width="22" height="22" viewBox="0 0 22 22"><circle cx="11" cy="11" r="9.5" fill="none" stroke="#fff" stroke-width="2"/><path d="M6.5 11.5l3 3 6-6.5" fill="none" stroke="#fff" stroke-width="2"/></svg>Visitor Analytics</li>
      <li><svg width="22" height="22" viewBox="0 0 22 22"><circle cx="11" cy="11" r="9.5" fill="none" stroke="#fff" stroke-width="2"/><path d="M6.5 11.5l3 3 6-6.5" fill="none" stroke="#fff" stroke-width="2"/></svg>Digital real estate solutions</li>
      <li><svg width="22" height="22" viewBox="0 0 22 22"><circle cx="11" cy="11" r="9.5" fill="none" stroke="#fff" stroke-width="2"/><path d="M6.5 11.5l3 3 6-6.5" fill="none" stroke="#fff" stroke-width="2"/></svg>Media sales digital communication in store</li>
    </ul>
  </div>
  <div class="slide-footer footer-on-dark" style="top:587px;">
    <span class="footer-mark">SLA</span><span class="footer-rule"></span><span class="page-no inverse">4</span>
  </div>
</section>

<!-- Slide 5 -->
<section class="slide feature">
  <div class="band"></div>
  <div class="photo" role="img" aria-label="Close-up of two hands joining white puzzle pieces"></div>
  <h2>Neque porro Quisquam<br>Est qui Dolorem</h2>
  <div class="body">Digital transformation is changing the way we live, what we<br>do and how we communicate with each other as well as how<br>we do our business and shopping.</div>
  <div class="slide-footer footer-on-light" style="top:603px;">
    <span class="footer-mark" style="color:var(--white);">SLA</span><span class="footer-rule"></span><span class="page-no filled">5</span>
  </div>
</section>

<!-- Slide 6 -->
<section class="slide contact" role="img" aria-label="Silhouettes of business people in a meeting, tinted dark blue">
  <div class="brand-mark" style="left:496px; top:145px; font-size:82px;">SLA</div>
  <div class="brand-name" style="top:266px; font-size:37px;">Summit Lane Advisors</div>
  <div class="brand-tagline" style="top:309px; font-size:20px;">We create competitiveness</div>

  <div class="contact-line" style="top:392px;">
    <svg width="18" height="24" viewBox="0 0 18 24"><path d="M9 0a9 9 0 0 0-9 9c0 7 9 15 9 15s9-8 9-15a9 9 0 0 0-9-9zm0 12.5A3.5 3.5 0 1 1 9 5.5a3.5 3.5 0 0 1 0 7z" fill="#fff"/></svg>
    <span>c/o Harbor Works House Kvarngatan 14 211 42 MALMÖ</span>
  </div>
  <div class="contact-line" style="top:438px;">
    <svg width="20" height="20" viewBox="0 0 20 20"><path d="M4 1l4 4-2 3c1 3 3 5 6 6l3-2 4 4-3 3C9 19 1 11 1 4z" fill="#fff"/></svg>
    <span>+46-701234567</span>
  </div>
  <div class="contact-line" style="top:483px;">
    <svg width="22" height="16" viewBox="0 0 22 16"><rect x="0" y="0" width="22" height="16" rx="2" fill="#fff"/><path d="M1 1l10 8 10-8" fill="none" stroke="#10306b" stroke-width="2"/></svg>
    <span>info@summitlaneadvisors.se</span>
  </div>
</section>

</body>
</html>
```